Church needs a street sign design

We're a small church located in Silicon Valley, California. Our website is https://www.hfbmerrow.org/ and our address is 4817 Larkfield Ave, San Jose, California, 95873. You can look up our location on Google Maps to see the sign from Street View. I have uploaded an image of the street sign as well. The marquee, the top section of the sign, and the separating line between them both will be removed. We're seeking a design for a new backlit acrylic insert that will go on the front of the light box and the back of the lightbox. The acrylic sign will fill the entire external frame. In the future, we may build a decorative wood frame around the structural legs, as visualized in one of the uploaded files. The church's brand colors are: #003366 (dark blue), #ff6600 (vibrant orange), #228b22 (forest green). I have also uploaded the church's logo assets. Our primary font is Montserrat and the secondary is Poppins. You can deviate from these colors/fonts if the sign is still coherent with the rest of our branding. Our branding values are mission, truth, passion, and community (please do not put those words on the sign! They are just intended to guide the look of the design). The sign dimensions are 96" by 47.5". Keep in mind that the sign will be backlit on a busy street side. It will also be positioned next to an old-looking church building. We do NOT want a sign that looks traditional, old, or antiquated. Instead, we want a modern-looking sign that pairs well with our old building while helping it look more modern too. We would also like the web address clearly visible on the sign: hfbmerrow.org. If you have any questions, just let me know!

```html
<!DOCTYPE html>
<html lang="en">
<head>
<meta charset="UTF-8">
<title>Hillside Fellowship Church – Street Sign</title>
<link href="https://fonts.googleapis.com/css2?family=Montserrat:wght@500;600&display=swap" rel="stylesheet">
<style>
  :root {
    --backdrop: #6e6e6e;
    --orange-top: #f26522;
    --orange-mid: #f7951f;
    --orange-low: #f68a1f;
    --orange-base: #f04e23;
    --glow: rgba(255, 205, 110, 0.55);
    --haze: rgba(255, 225, 160, 0.35);
    --shade: rgba(225, 95, 20, 0.35);
    --navy: #1f3f7a;
    --navy-deep: #14306a;
    --white: #ffffff;
    --ink: #111111;
  }
  * { margin: 0; padding: 0; box-sizing: border-box; }
  html, body {
    width: 1200px;
    height: 1200px;
    overflow: hidden;
    background: var(--backdrop);
    font-family: "Montserrat", sans-serif;
  }
  .sign {
    position: absolute;
    left: 354px;
    top: 102px;
    width: 492px;
    height: 994px;
    overflow: hidden;
  }
  .sign-photo {
    position: absolute;
    inset: 0;
    background:
      radial-gradient(ellipse 34% 30% at 50% 57%, var(--glow), rgba(255,205,110,0) 75%),
      radial-gradient(ellipse 70% 14% at 50% 80%, var(--haze), rgba(255,225,160,0) 80%),
      linear-gradient(90deg, var(--shade) 0%, rgba(225,95,20,0) 12%, rgba(255,200,100,0.18) 14%, rgba(255,200,100,0) 22%, rgba(255,200,100,0) 78%, rgba(255,200,100,0.18) 86%, rgba(225,95,20,0) 88%, var(--shade) 100%),
      linear-gradient(180deg, var(--orange-top) 0%, var(--orange-mid) 40%, var(--orange-low) 70%, var(--orange-base) 100%);
  }
  .sign-photo::before {
    content: "";
    position: absolute;
    left: 22%;
    right: 22%;
    top: 38%;
    bottom: 20%;
    background: linear-gradient(180deg, rgba(255,215,130,0) 0%, rgba(255,215,130,0.28) 35%, rgba(255,215,130,0.2) 100%);
    filter: blur(18px);
  }
  .brand {
    position: absolute;
    left: 44px;
    top: 190px;
    display: flex;
    align-items: center;
    gap: 22px;
  }
  .brand-mark {
    width: 50px;
    height: 50px;
    background: var(--white);
    flex: none;
  }
  .brand-name {
    color: var(--white);
    font-weight: 600;
    line-height: 1;
  }
  .brand-name .primary {
    display: block;
    font-size: 58px;
    letter-spacing: 0.5px;
  }
  .brand-name .secondary {
    display: block;
    margin-top: 12px;
    font-size: 20px;
    letter-spacing: 0.3px;
  }
  .address {
    position: absolute;
    left: 0;
    right: 0;
    top: 743px;
    text-align: center;
    color: var(--ink);
    font-weight: 500;
    font-size: 27px;
    line-height: 35px;
  }
  .web-banner {
    position: absolute;
    left: 0;
    top: 869px;
    width: 492px;
    height: 48px;
  }
  .web-banner svg { position: absolute; inset: 0; }
  .web-address {
    position: relative;
    display: block;
    text-align: center;
    line-height: 48px;
    color: var(--white);
    font-weight: 500;
    font-size: 29px;
  }
</style>
</head>
<body>
  <main class="sign">
    <div class="sign-photo" role="img" aria-label="Photo of a person standing with arms outstretched in a bright doorway, tinted warm orange"></div>

    <div class="brand">
      <span class="brand-mark" aria-hidden="true"></span>
      <div class="brand-name">
        <span class="primary">HILLSIDE</span>
        <span class="secondary">FELLOWSHIP CHURCH</span>
      </div>
    </div>

    <p class="address">4817 Larkfield Ave, San Jose,<br>California, 95873</p>

    <div class="web-banner">
      <svg width="492" height="48" viewBox="0 0 492 48" aria-hidden="true">
        <defs>
          <linearGradient id="bannerFill" x1="0" y1="0" x2="1" y2="0">
            <stop offset="0" stop-color="#14306a"/>
            <stop offset="0.5" stop-color="#1f3f7a"/>
            <stop offset="1" stop-color="#14306a"/>
          </linearGradient>
        </defs>
        <polygon points="0,24 22,0 470,0 492,24 470,48 22,48" fill="url(#bannerFill)"/>
      </svg>
      <span class="web-address">www.hfbmerrow.org</span>
    </div>
  </main>
</body>
</html>
```